KINDLE: Social Media Post COVID-19 & Flu #2

- Please use or create a similar design as before and create a Social Media Post.
- Attached, Logo, sample flu social media image.
- KINDLE - must be included - in the colors provided (see attachment)
- Protect your community. Protect Your Elders. Stay Vaccinated. - must be include
-COVID-19 & flu - should be included
- image of child and women - should be included
-might include border
- inspiration https://temvora.example/, and https://www.facebook.com/Temvora

```html
<!DOCTYPE html>
<html lang="en">
<head>
<meta charset="utf-8">
<title>KINDLE – COVID-19 &amp; Flu Vaccination Campaign</title>
<link rel="stylesheet" href="https://fonts.googleapis.com/css2?family=Montserrat:wght@600;800;900&family=Merriweather:wght@700&display=swap">
<style>
  :root {
    --teal: #4ea6ae;
    --maroon: #8c2a37;
    --white: #ffffff;
    --border-tone: #b9c4c6;
    --grass: #7fbf2a;
    --grass-deep: #5c9a1c;
  }
  * { margin: 0; padding: 0; box-sizing: border-box; }
  html, body { width: 1200px; height: 1196px; overflow: hidden; background: var(--white); }
  .post {
    position: relative;
    width: 1200px;
    height: 1196px;
    background: var(--border-tone);
    font-family: "Montserrat", sans-serif;
  }
  .pattern-border {
    position: absolute; inset: 0;
    background: linear-gradient(135deg, #c7a3a8, #a9c2c5 50%, #c7a3a8);
  }
  .frame {
    position: absolute;
    left: 34px; top: 34px; width: 1132px; height: 1128px;
    border: 9px solid var(--maroon);
    background: var(--white);
  }
  .scene {
    position: absolute;
    left: 43px; top: 43px; width: 1114px; height: 1110px;
    background:
      radial-gradient(ellipse 280px 420px at 960px 560px, rgba(70,130,220,.85), rgba(70,130,220,0) 70%),
      radial-gradient(ellipse 260px 520px at 120px 480px, rgba(40,90,210,.85), rgba(40,90,210,0) 70%),
      radial-gradient(ellipse 260px 200px at 760px 340px, rgba(220,80,40,.7), rgba(220,80,40,0) 70%),
      linear-gradient(180deg, #b9a98a 0%, #d9c7a2 14%, #c98a5a 28%, #a8b050 42%, var(--grass) 55%, var(--grass-deep) 100%);
  }
  .title-frame {
    position: absolute;
    left: 83px; top: 81px; width: 732px; height: 181px;
    border: 7px solid var(--maroon);
  }
  .title {
    position: absolute;
    left: 116px; top: 96px;
    font-weight: 800;
    font-size: 126px;
    line-height: 1;
    letter-spacing: 6px;
    color: var(--teal);
  }
  .campaign-band {
    position: absolute;
    left: 135px; top: 227px; width: 627px; height: 53px;
    background: var(--maroon);
    color: var(--white);
    font-family: "Merriweather", serif;
    font-weight: 700;
    font-size: 24px;
    letter-spacing: 1.5px;
    display: flex; align-items: center; justify-content: center;
  }
  .brand {
    position: absolute;
    left: 872px; top: 150px;
    display: flex; align-items: center; gap: 12px;
    font-weight: 800;
    font-size: 40px;
    color: var(--teal);
  }
  .brand-mark { width: 26px; height: 26px; background: var(--maroon); }
  .glow-band {
    position: absolute;
    background: rgba(255,255,255,.28);
  }
  .glow-one { left: 87px; top: 345px; width: 571px; height: 90px; }
  .glow-two { left: 87px; top: 575px; width: 571px; height: 90px; }
  .glow-three { left: 37px; top: 851px; width: 1080px; height: 121px; }
  .line {
    position: absolute;
    font-weight: 900;
    line-height: 1;
    -webkit-text-stroke: 7px var(--white);
    paint-order: stroke fill;
    text-shadow: 2px 3px 4px rgba(0,0,0,.25);
  }
  .line-teal { color: var(--teal); }
  .line-maroon { color: var(--maroon); }
  .protect-community { left: 102px; top: 356px; font-size: 70px; }
  .community { left: 102px; top: 450px; font-size: 78px; }
  .protect-elders { left: 102px; top: 582px; font-size: 70px; }
  .elders { left: 102px; top: 678px; font-size: 78px; }
  .stay-vaccinated { left: 92px; top: 862px; font-size: 102px; }
  .info-bar {
    position: absolute;
    left: 37px; top: 1019px; width: 1120px; height: 90px;
    background: var(--maroon);
    color: var(--white);
    font-weight: 600;
    font-size: 27px;
    letter-spacing: 1.2px;
    display: flex; align-items: center; justify-content: center;
  }
</style>
</head>
<body>
  <main class="post">
    <div class="pattern-border" role="img" aria-label="Chevron zigzag border pattern in teal and maroon"></div>
    <div class="frame"></div>
    <div class="scene" role="img" aria-label="Photo of a powwow: a woman in a blue shawl and a young girl in colourful regalia walking on green grass toward dancers and tents"></div>

    <div class="title-frame"></div>
    <h1 class="title">KINDLE</h1>
    <div class="campaign-band">COVID-19 &amp; FLU VACCINATION CAMPAIGN</div>

    <div class="brand"><span class="brand-mark"></span>TEMVORA</div>

    <div class="glow-band glow-one"></div>
    <div class="glow-band glow-two"></div>
    <div class="glow-band glow-three"></div>

    <p class="line line-teal protect-community">Protect Your</p>
    <p class="line line-maroon community">Community</p>
    <p class="line line-teal protect-elders">Protect Your</p>
    <p class="line line-maroon elders">Elders</p>
    <p class="line line-teal stay-vaccinated">Stay Vaccinated</p>

    <div class="info-bar">Learn more about getting vaccinated against COVID-19 &amp; the Flu</div>
  </main>
</body>
</html>
```